Bakery looking for new Business cards

I have a new logo and now its time to upgrade our business cards.
e-mail - info@corvelbakehouse.com
www.corvelbakehouse.com
847-619-2837

518w Pellow Brook rd. Dunmoor OH 60473
Bakery Hour's Tuesday-Saturday 8am-5pm

Industry/Entity Type

Bakery

Contact Information for Business Card

Hr's

Requirements
Must have
• Business information.
Nice to have
• would like to include a QR code for our website.

```html
<!DOCTYPE html>
<html lang="en">
<head>
<meta charset="utf-8">
<title>Corvel Bakehouse – Business Cards</title>
<link rel="stylesheet" href="https://fonts.googleapis.com/css2?family=Montserrat:wght@400;500;600;700&display=swap">
<style>
  :root {
    --page-bg: #e9e5df;
    --card-white: #ffffff;
    --card-black: #111111;
    --ink: #1c1c1c;
    --gold: #e0a33a;
    --band-dark: #2a2a2a;
    --back-text: #f2f2f2;
    --back-name: #5a5a5a;
  }
  * { box-sizing: border-box; margin: 0; padding: 0; }
  html, body {
    width: 900px; height: 1200px; overflow: hidden;
    background: var(--page-bg);
    font-family: "Montserrat", sans-serif;
    color: var(--ink);
  }
  .canvas { position: relative; width: 900px; height: 1200px; }

  .card {
    position: absolute; width: 742px; height: 442px;
    border-radius: 22px; overflow: hidden;
    box-shadow: 0 10px 24px rgba(0,0,0,0.25);
  }
  .card--front { left: 80px; top: 130px; background: var(--card-white); }
  .card--back { left: 78px; top: 638px; background: var(--card-black); }

  .brand {
    position: absolute; left: 50px; width: 300px; top: 262px;
    display: flex; align-items: center; justify-content: center; gap: 10px;
  }
  .brand__dot { width: 12px; height: 12px; border-radius: 50%; background: var(--gold); flex: none; }
  .brand__name { font-size: 24px; font-weight: 600; color: var(--ink); white-space: nowrap; }

  .divider { position: absolute; left: 357px; top: 110px; width: 2px; height: 215px; background: var(--gold); }

  .contact { position: absolute; left: 373px; top: 112px; }
  .contact__name { font-size: 26px; font-weight: 700; color: var(--gold); line-height: 1.1; }
  .contact__role { font-size: 15.5px; font-weight: 400; margin-top: 2px; }
  .contact__list { list-style: none; margin-top: 20px; }
  .contact__item { display: flex; align-items: center; gap: 10px; font-size: 15.5px; height: 30px; }
  .contact__item svg { width: 16px; height: 16px; fill: var(--gold); flex: none; }
  .contact__address { font-size: 15.5px; line-height: 21px; margin-top: 12px; }

  .band { position: absolute; left: 0; bottom: 0; width: 742px; height: 22px; }

  .back-brand {
    position: absolute; left: 0; right: 0; top: 180px;
    display: flex; align-items: center; justify-content: center; gap: 18px;
  }
  .back-brand__dot { width: 22px; height: 22px; border-radius: 50%; background: var(--back-name); }
  .back-brand__name { font-size: 54px; font-weight: 600; color: var(--back-name); white-space: nowrap; }

  .hours {
    position: absolute; left: 0; right: 0; top: 381px;
    text-align: center; font-size: 16px; color: var(--back-text);
  }
</style>
</head>
<body>
<main class="canvas">
  <section class="card card--front" aria-label="Business card front">
    <div class="brand">
      <span class="brand__dot"></span>
      <span class="brand__name">Corvel Bakehouse</span>
    </div>
    <div class="divider"></div>
    <div class="contact">
      <p class="contact__name">Mara Tolin</p>
      <p class="contact__role">Owner</p>
      <ul class="contact__list">
        <li class="contact__item">
          <svg viewBox="0 0 16 16" aria-hidden="true"><path d="M1 5c0-2 3-3 7-3s7 1 7 3v1h-4V5H5v1H1z"/><path d="M3 7h10l1 7H2z"/><circle cx="8" cy="10.5" r="2" fill="#fff"/></svg>
          847-619-2837
        </li>
        <li class="contact__item">
          <svg viewBox="0 0 16 16" aria-hidden="true"><path d="M1 3h14v1L8 9 1 4z"/><path d="M1 5.5l7 5 7-5V13H1z"/></svg>
          info@corvelbakehouse.com
        </li>
        <li class="contact__item">
          <svg viewBox="0 0 16 16" aria-hidden="true"><circle cx="8" cy="8" r="7"/><path d="M4 4c2 1 2 3 4 3s1 3 3 3M9 2c0 2 2 2 4 3" stroke="#fff" stroke-width="1.2" fill="none"/></svg>
          www.corvelbakehouse.com
        </li>
      </ul>
      <p class="contact__address">518w Pellow Brook rd.<br>Dunmoor OH 60473</p>
    </div>
    <svg class="band" viewBox="0 0 742 22" aria-hidden="true">
      <polygon points="0,0 358,0 345,22 0,22" fill="var(--band-dark)"/>
      <polygon points="370,0 742,0 742,22 357,22" fill="var(--gold)"/>
    </svg>
  </section>

  <section class="card card--back" aria-label="Business card back">
    <div class="back-brand">
      <span class="back-brand__dot"></span>
      <span class="back-brand__name">Corvel Bakehouse</span>
    </div>
    <p class="hours">Bakery Hour's Tuesday-Saturday 8am-5pm</p>
  </section>
</main>
</body>
</html>
```